Business card for Eyelash extension salon in Marlowe Hills,California USA

We need new business card for our salon in Marlowe Hills. The salon name is 'Lumarra' . We would like to have...Business name: Lumarra Name of person: will provide later Address 6128 N.Corbel Ridge Blvd Marlowe Hills , CA 90417 Phone: will provide later (Text only) Web: www.lumarrastudio-example.com Pictogrid icon, Friendvale icon follow us for seasonal campaign and news @lumarrastudioexample Design should look elegant, high-end, clean, simple, cohesive with my brand. Please refer my brand board. Business name color will be metallic bronzy color. Im thinking grey background or white background. Thanks

Target Market(s)

25-35. Gender neutral. People who are in Entertainment business industry.
This is High-end Eyelash extension salon in Marlowe Hills

Industry/Entity Type

Beauty Salon

Contact Information for Business Card

Business name: Lumarra
Name of person: will provide later
Address 6128 N.Corbel Ridge Blvd Marlowe Hills , CA 90417
Phone: will provide later (Text only)
Web: www.lumarrastudio-example.com
Pictogrid icon, Friendvale icon
follow us for seasonal campaign and news @lumarrastudioexample

Requirements
Must have
• Beautiful, elegant, clean and simple look but very attractive and modern
Should not have
• We don't like too clutter, too busy designs.

```html
<!DOCTYPE html>
<html lang="en">
<head>
<meta charset="utf-8">
<title>Lumarra Business Card</title>
<link href="https://fonts.googleapis.com/css2?family=Lato:wght@300;400;700&display=swap" rel="stylesheet">
<style>
  :root {
    --page-bg: #e4e6e6;
    --card-dark: #191c1c;
    --card-light: #ffffff;
    --bronze: #b4967c;
    --bronze-deep: #8a6547;
    --muted-grey: #6c7070;
    --ink: #4a5557;
    --accent-cyan: #22c4e8;
  }
  * { box-sizing: border-box; margin: 0; padding: 0; }
  html, body { width: 1200px; height: 1200px; overflow: hidden; }
  body {
    background: var(--page-bg);
    font-family: "Lato", Helvetica, Arial, sans-serif;
    position: relative;
  }
  .card {
    position: absolute;
    width: 604px;
    height: 345px;
    box-shadow: 0 6px 10px rgba(0,0,0,0.28);
  }
  .card--front { left: 298px; top: 190px; background: var(--card-dark); }
  .card--back  { left: 300px; top: 600px; background: var(--card-light); }

  .wordmark { position: absolute; font-weight: 300; line-height: 1; }
  .wordmark__name { display: block; }
  .wordmark__place {
    display: block;
    text-transform: uppercase;
    font-weight: 400;
  }
  .card--front .wordmark { left: 0; width: 604px; top: 105px; text-align: center; color: var(--bronze); }
  .card--front .wordmark__name { font-size: 84px; letter-spacing: 2px; }
  .card--front .wordmark__place { font-size: 11px; letter-spacing: 3px; margin-top: 16px; padding-left: 150px; }

  .card--back .wordmark { right: 40px; top: 52px; text-align: right; color: var(--bronze-deep); }
  .card--back .wordmark__name { font-size: 48px; letter-spacing: 1px; }
  .card--back .wordmark__place { font-size: 7px; letter-spacing: 1.5px; margin-top: 10px; }

  .social { position: absolute; left: 62px; top: 262px; color: var(--muted-grey); font-size: 14px; }
  .social__row { display: flex; align-items: center; gap: 12px; }
  .social__network { display: flex; align-items: center; gap: 6px; }
  .social__dot { width: 12px; height: 12px; background: var(--muted-grey); }
  .social__dot--round { border-radius: 50%; }
  .social__tagline { margin-top: 10px; padding-left: 6px; }

  .person { position: absolute; left: 31px; top: 130px; }
  .person__name { font-size: 24px; font-weight: 700; color: var(--ink); letter-spacing: -0.3px; }
  .person__first { color: var(--accent-cyan); }
  .person__role {
    display: flex; align-items: flex-end;
    width: 525px; font-size: 14.5px; color: var(--ink); margin-top: 4px;
  }
  .person__leader { flex: 1; border-bottom: 1px dotted var(--ink); margin: 0 0 3px 3px; }

  .contact { position: absolute; right: 38px; top: 196px; text-align: right; color: var(--ink); font-size: 15px; }
  .contact__line { display: flex; justify-content: flex-end; gap: 8px; line-height: 22px; letter-spacing: 0.3px; }
  .contact__label { color: var(--accent-cyan); font-size: 13px; width: 16px; text-align: left; }
  .contact__hl { color: var(--accent-cyan); }

  .address { position: absolute; left: 34px; top: 272px; color: var(--ink); font-size: 14px; line-height: 18px; font-style: normal; }
  .address__city { padding-left: 52px; }
</style>
</head>
<body>
  <section class="card card--front" aria-label="Card front">
    <div class="wordmark">
      <span class="wordmark__name">Lumarra</span>
      <span class="wordmark__place">Marlowe Hills</span>
    </div>
    <div class="social">
      <div class="social__row">
        <span class="social__network"><span class="social__dot"></span>Friendvale</span>
        <span class="social__network"><span class="social__dot social__dot--round"></span>Pictogrid</span>
        <span>@lumarrastudioexample</span>
      </div>
      <p class="social__tagline">follow us for seasonal campaign and news</p>
    </div>
  </section>

  <section class="card card--back" aria-label="Card back">
    <div class="wordmark">
      <span class="wordmark__name">Lumarra</span>
      <span class="wordmark__place">Marlowe Hills</span>
    </div>
    <div class="person">
      <h1 class="person__name"><span class="person__first">Dorian</span> Vale</h1>
      <p class="person__role">Founder and CEO<span class="person__leader"></span></p>
    </div>
    <div class="contact">
      <p class="contact__line"><span>0000000000</span><span class="contact__label">:p</span></p>
      <p class="contact__line"><span><span class="contact__hl">info</span>@lumarrastudio-example.com</span><span class="contact__label">:E</span></p>
      <p class="contact__line"><span>lumarrastudio-example.com</span><span class="contact__label">:w</span></p>
    </div>
    <address class="address">
      <div>6128 N.Corbel Ridge Blvd Marlowe Hills ,</div>
      <div class="address__city">CA 90417</div>
    </address>
  </section>
</body>
</html>
```